roofing door hanger

we would like to have our logo kvt roofing, it would be given when we are working in the neighborhood and have our services roof replacement, roof repair, ventilation, inspections. Our slogan is "Reliability starts at the top" . Our company is kvt roofing i would like to get one or two reviews from vorblin, and f any pictures are needed can use pellomart.

Industry/Entity Type

Roofing

Requirements
Must have
• this has to be a door hanger design

```html
<!DOCTYPE html>
<html lang="en">
<head>
<meta charset="utf-8">
<title>KVT Roofing – Door Hanger</title>
<link rel="stylesheet" href="https://fonts.googleapis.com/css2?family=Open+Sans:wght@600;700;800&display=swap">
<style>
  :root {
    --backdrop: #3a3a3c;
    --brand-orange: #f5861f;
    --headline-orange: #f0851c;
    --panel-light: #f5f6f8;
    --panel-mid: #e7e9ec;
    --wave-grey: #d4d6da;
    --text-grey: #5d5f63;
    --logo-grey: #8b8d91;
    --white: #ffffff;
  }
  html, body {
    margin: 0;
    padding: 0;
    width: 718px;
    height: 1200px;
    overflow: hidden;
    background: var(--backdrop);
  }
  .door-hanger {
    position: absolute;
    left: 129px;
    top: 41px;
    width: 460px;
    height: 1118px;
    display: block;
    font-family: "Open Sans", Arial, sans-serif;
  }
  .headline { fill: var(--headline-orange); font-weight: 800; font-size: 25px; letter-spacing: -0.3px; }
  .services-title { fill: var(--white); font-weight: 700; font-size: 12px; }
  .service-item { fill: var(--white); font-weight: 600; font-size: 12px; }
  .service-bullet { fill: var(--brand-orange); stroke: var(--white); stroke-width: 0.8; }
  .brand-name { fill: var(--logo-grey); font-weight: 800; font-size: 27px; letter-spacing: 0.5px; }
  .brand-mark { fill: var(--brand-orange); }
  .call-line { fill: var(--text-grey); font-weight: 700; font-size: 12.5px; }
  .call-phone { fill: var(--brand-orange); font-weight: 800; font-size: 16.5px; }
  .web-address { fill: var(--brand-orange); font-weight: 700; font-size: 12px; letter-spacing: 1px; }
</style>
</head>
<body>
<svg class="door-hanger" viewBox="0 0 298 724" xmlns="http://www.w3.org/2000/svg" aria-label="KVT Roofing door hanger">
  <defs>
    <linearGradient id="panelGradient" x1="0" y1="0" x2="0" y2="1">
      <stop offset="0" stop-color="var(--panel-light)"/>
      <stop offset="1" stop-color="var(--panel-mid)"/>
    </linearGradient>
    <linearGradient id="mainPhotoTone" x1="0" y1="0" x2="0.3" y2="1">
      <stop offset="0" stop-color="#e9e4df"/>
      <stop offset="0.45" stop-color="#b9b4ae"/>
      <stop offset="0.7" stop-color="#4b4d52"/>
      <stop offset="1" stop-color="#3c3d41"/>
    </linearGradient>
    <linearGradient id="detailPhotoTone" x1="0" y1="0" x2="1" y2="1">
      <stop offset="0" stop-color="#9aa3b0"/>
      <stop offset="1" stop-color="#55585e"/>
    </linearGradient>
    <linearGradient id="toolsPhotoTone" x1="0" y1="0" x2="1" y2="1">
      <stop offset="0" stop-color="#dfe3e8"/>
      <stop offset="1" stop-color="#5a5e66"/>
    </linearGradient>
  </defs>

  <!-- hanger body -->
  <rect class="hanger-body" x="0" y="0" width="298" height="724" fill="url(#panelGradient)"/>

  <!-- top band with wave -->
  <path class="wave-shadow" fill="var(--wave-grey)"
        d="M0 178 C 50 168, 90 182, 140 190 C 200 200, 250 176, 298 172 V186 C 250 190, 200 212, 140 204 C 90 196, 50 182, 0 192 Z"/>
  <path class="top-band" fill="var(--brand-orange)"
        d="M0 0 H298 V166 C 250 168, 200 194, 140 186 C 90 180, 50 166, 0 180 Z"/>

  <!-- door hole and slit -->
  <line class="hanger-slit" x1="0" y1="149" x2="96" y2="110" stroke="var(--backdrop)" stroke-width="4"/>
  <circle class="hanger-hole" cx="150" cy="93" r="63" fill="var(--backdrop)"/>

  <!-- slogan -->
  <text class="headline" x="149" y="237" text-anchor="middle">RELIABILITY</text>
  <text class="headline" x="149" y="268" text-anchor="middle">STARTS AT THE TOP</text>

  <!-- main photo -->
  <g role="img" aria-label="Photo of a roofer in a hard hat and safety vest working on shingles">
    <circle class="main-photo" cx="150" cy="436" r="137" fill="url(#mainPhotoTone)" stroke="var(--brand-orange)" stroke-width="5"/>
  </g>

  <!-- detail photos -->
  <g role="img" aria-label="Close-up photo of hands laying roof shingles">
    <circle class="detail-photo" cx="65" cy="346" r="43" fill="url(#detailPhotoTone)" stroke="var(--white)" stroke-width="3"/>
    <circle cx="65" cy="346" r="45.5" fill="none" stroke="var(--brand-orange)" stroke-width="1.5"/>
  </g>
  <g role="img" aria-label="Photo of roofing tools">
    <circle class="detail-photo" cx="245" cy="545" r="43" fill="url(#toolsPhotoTone)" stroke="var(--white)" stroke-width="3"/>
    <circle cx="245" cy="545" r="45.5" fill="none" stroke="var(--brand-orange)" stroke-width="1.5"/>
  </g>

  <!-- services -->
  <g class="services-list">
    <text class="services-title" x="64" y="464">Our Services</text>
    <circle class="service-bullet" cx="68" cy="482" r="4"/>
    <text class="service-item" x="79" y="486">Roof Replacement</text>
    <circle class="service-bullet" cx="68" cy="499" r="4"/>
    <text class="service-item" x="79" y="503">Roof Repair</text>
    <circle class="service-bullet" cx="68" cy="516" r="4"/>
    <text class="service-item" x="79" y="520">Ventilation</text>
    <circle class="service-bullet" cx="68" cy="533" r="4"/>
    <text class="service-item" x="79" y="537">Inspections</text>
  </g>

  <!-- brand -->
  <g class="brand">
    <rect class="brand-mark" x="141" y="596" width="16" height="16"/>
    <text class="brand-name" x="149" y="650" text-anchor="middle">KVT ROOFING</text>
  </g>

  <!-- contact -->
  <text x="149" y="689" text-anchor="middle">
    <tspan class="call-line">Call for a quote today: </tspan><tspan class="call-phone">555-014-2287</tspan>
  </text>
  <text class="web-address" x="149" y="710" text-anchor="middle">www.kvt-roofing.com</text>
</svg>
</body>
</html>
```